Business Card Design Project

Build kick ass business card.
Updates

I just uploaded the Vorintex Logo in AI format, for those that were asking. It's looking real good and we'll be reviewing the designs soon. Thanks. 

Target Market(s)

Businesses in many verticals. Focusing on information security.

Vorintex, LLC
Gordon Bexley
Principal Security Consultant
Mobile: +1-602-555-0187
Email: Gordon.Bexley@Vorintex.example
Web: www.vorintex.example

Industry/Entity Type

Business

Requirements
Must have
• Design must look high-end, hi-tech stylish and minimalist

Be different – one that stands out from thousands of others

Does not have to be traditional rectangle

Would like logo integrated

```html
<!DOCTYPE html>
<html lang="en">
<head>
<meta charset="utf-8">
<title>Vorintex Business Card</title>
<link rel="stylesheet" href="https://fonts.googleapis.com/css2?family=Open+Sans:wght@300;400&display=swap">
<style>
  :root {
    --page-bg: #e9e9e9;
    --card-top: #f7f7f7;
    --card-bottom: #d4d4d4;
    --card-edge: #8f8f8f;
    --window-fill: #e3e3e3;
    --window-shade: #b8b8b8;
    --tab-top: #fafafa;
    --tab-bottom: #d9d9d9;
    --ink: #1e1e1e;
    --rule: #6a6a6a;
    --accent: #1b98d5;
  }
  * { box-sizing: border-box; margin: 0; padding: 0; }
  html, body {
    width: 1200px;
    height: 675px;
    overflow: hidden;
    background: var(--page-bg);
    font-family: "Open Sans", Arial, sans-serif;
    color: var(--ink);
  }
  .canvas {
    position: relative;
    width: 1200px;
    height: 675px;
  }
  .card {
    position: absolute;
    left: 320px;
    top: 130px;
    width: 560px;
    height: 420px;
    border-radius: 44px;
    background: linear-gradient(180deg, var(--card-top), var(--card-bottom));
    border: 1.5px solid var(--card-edge);
    box-shadow: 0 10px 28px rgba(0,0,0,0.18);
  }
  .card-window {
    position: absolute;
    left: 44px;
    top: 22px;
    width: 472px;
    height: 130px;
    border-radius: 30px;
    background: var(--window-fill);
    box-shadow: inset 0 4px 10px var(--window-shade);
  }
  .logo-tab {
    position: absolute;
    left: 72px;
    top: 12px;
    width: 320px;
    height: 108px;
    border-radius: 26px;
    background: linear-gradient(180deg, var(--tab-top), var(--tab-bottom));
    border: 1px solid var(--card-edge);
    box-shadow: 0 6px 12px rgba(0,0,0,0.22);
    display: flex;
    align-items: center;
    justify-content: center;
    gap: 16px;
  }
  .logo-dot {
    width: 30px;
    height: 30px;
    border-radius: 50%;
    background: var(--accent);
  }
  .logo-name {
    font-size: 38px;
    font-weight: 400;
    color: var(--ink);
    letter-spacing: 1px;
  }
  .contact {
    position: absolute;
    left: 0;
    right: 0;
    top: 172px;
    text-align: center;
    font-weight: 400;
  }
  .company { font-size: 19px; line-height: 24px; }
  .person { font-size: 29px; font-weight: 300; line-height: 38px; }
  .divider {
    width: 300px;
    height: 1px;
    margin: 2px auto 10px;
    background: linear-gradient(90deg, transparent, var(--rule), transparent);
  }
  .role, .line { font-size: 19px; line-height: 32px; }
</style>
</head>
<body>
<main class="canvas">
  <section class="card" aria-label="Business card">
    <div class="card-window"></div>
    <div class="logo-tab">
      <span class="logo-dot"></span>
      <span class="logo-name">Vorintex</span>
    </div>
    <div class="contact">
      <p class="company">Vorintex, LLC</p>
      <p class="person">Gordon Bexley</p>
      <div class="divider"></div>
      <p class="role">Principal Security Consultant</p>
      <p class="line">Mobile: +1-602-555-0187</p>
      <p class="line">Email: Gordon.Bexley@Vorintex.example</p>
      <p class="line">Web: www.vorintex.example</p>
    </div>
  </section>
</main>
</body>
</html>
```